Flyer

I am a qualified accountant and I need a flyer to promote my business when networking

My services include
Management Accounts, Financial Accounts, Day to Day Bookkeeping services, business start up assistance
I will produce and submit Self Assessment Tax Returns, Annual Accounts, VAT tax returns, Payroll and PAYE

I attach my business card design so that there is some continuity if you think it appropiate.

Size A3 is preferred, please.

Sorry, I mean't Size A5 is preferred.

A5 please

Free initial consultations and advice.

```html
<!DOCTYPE html>
<html lang="en">
<head>
<meta charset="utf-8">
<title>Clara Benton Accounting – Flyer</title>
<link rel="stylesheet" href="https://fonts.googleapis.com/css2?family=Nunito+Sans:wght@300;400;700&family=Cinzel:wght@400;600&display=swap">
<style>
  :root {
    --green: #8dc63f;
    --green-dark: #7ab32e;
    --red: #e03c31;
    --ink: #231f20;
    --paper: #ffffff;
    --photo-light: #e4e4e4;
    --photo-mid: #9a9a9a;
    --photo-dark: #3a3a3a;
  }
  * { margin: 0; padding: 0; box-sizing: border-box; }
  html, body { width: 847px; height: 1200px; overflow: hidden; background: var(--paper); }
  body { font-family: "Nunito Sans", Arial, sans-serif; color: var(--ink); }
  .flyer { position: relative; width: 847px; height: 1200px; overflow: hidden; background: var(--paper); }

  .figure-band {
    position: absolute; left: 0; top: 0; width: 847px; height: 92px;
    background: linear-gradient(90deg, #a6d45a, var(--green) 50%, #9bcf4e);
  }
  .hero-photo {
    position: absolute; left: 0; top: 92px; width: 847px; height: 420px;
    background: radial-gradient(ellipse at 30% 60%, var(--photo-light) 0%, #c9c9c9 35%, var(--photo-mid) 65%, var(--photo-dark) 100%);
  }
  .hero-shape { position: absolute; left: 0; top: 92px; width: 847px; height: 430px; }

  .headline { position: absolute; left: 353px; top: 180px; color: var(--paper); font-weight: 300; text-transform: uppercase; }
  .headline .lead { display: block; font-size: 29px; letter-spacing: 1.5px; }
  .headline .focus { display: block; font-size: 44px; letter-spacing: 3px; margin-top: 2px; margin-left: 60px; }

  .tagline { position: absolute; left: 36px; top: 510px; font-size: 25px; font-weight: 400; line-height: 44px; text-transform: uppercase; letter-spacing: 0.3px; }

  .section-bar { position: absolute; left: 36px; top: 614px; width: 744px; height: 34px; }
  .section-bar span { position: absolute; left: 10px; top: 5px; color: var(--paper); font-size: 19px; }

  .intro { position: absolute; left: 36px; top: 670px; width: 380px; font-size: 23px; font-weight: 300; line-height: 33px; }

  .service-list { position: absolute; left: 448px; top: 692px; list-style: none; font-size: 21px; font-weight: 300; line-height: 30px; }
  .service-list li { position: relative; padding-left: 20px; }
  .service-list li::before { content: "•"; position: absolute; left: 0; }

  .offer { position: absolute; left: 36px; top: 948px; width: 347px; height: 56px; background: var(--green); color: var(--paper); font-size: 29px; font-weight: 400; line-height: 56px; text-align: center; }

  .brand { position: absolute; left: 80px; top: 1040px; width: 300px; display: flex; flex-direction: column; align-items: center; gap: 14px; }
  .brand-dot { width: 60px; height: 60px; border-radius: 50%; background: var(--green); }
  .brand-name { font-family: "Nunito Sans", Arial, sans-serif; font-size: 21px; font-weight: 400; color: var(--ink); text-transform: uppercase; letter-spacing: 1px; }

  .contact { position: absolute; left: 400px; top: 1036px; width: 440px; text-align: center; }
  .contact .call { color: var(--green-dark); font-weight: 700; font-size: 20px; }
  .contact .name { font-family: "Cinzel", Georgia, serif; font-size: 27px; font-weight: 400; color: var(--ink); margin-top: 2px; }
  .contact .phone { color: var(--red); font-size: 24px; letter-spacing: 1px; }
  .contact .email { color: var(--red); font-size: 18px; }
  .contact .web { color: var(--green-dark); font-size: 24px; margin-top: 4px; }
</style>
</head>
<body>
<main class="flyer">
  <div class="figure-band" role="img" aria-label="Green band filled with scattered numbers and maths symbols"></div>
  <div class="hero-photo" role="img" aria-label="Photo of a hand holding a pen beside a calculator"></div>

  <svg class="hero-shape" viewBox="0 0 847 430" aria-hidden="true">
    <path d="M0 406 L0 430 L847 430 L847 336 L545 336 C505 336 490 350 470 372 C450 396 430 406 400 406 Z" fill="#ffffff"/>
    <path d="M0 406 L400 406 C430 406 450 396 470 372 C490 350 505 336 545 336 L847 336" fill="none" stroke="#231f20" stroke-width="5"/>
  </svg>

  <h1 class="headline">
    <span class="lead">Take control of your</span>
    <span class="focus">Business</span>
  </h1>

  <p class="tagline">From basic book keeping to<br>more complex financial needs</p>

  <div class="section-bar">
    <svg width="744" height="34" viewBox="0 0 744 34" aria-hidden="true">
      <path d="M0 0 L420 0 C460 0 470 20 520 22 L744 24 L744 28 L500 30 C470 31 450 34 420 34 L0 34 Z" fill="#231f20"/>
    </svg>
    <span>SERVICES</span>
  </div>

  <p class="intro">I am a fully qualified accountant offering a friendly and professional service for all your accounting needs. Whether you need help with your personal finances and your are running a successful business I can help.</p>

  <ul class="service-list">
    <li>Management Accounting</li>
    <li>Financial Accounting</li>
    <li>Budgeting</li>
    <li>Day to Day Bookkeeping Services</li>
    <li>Production and submission of<br>Self Assessment Tax Returns</li>
    <li>VAT returns</li>
    <li>Annual Accounts</li>
    <li>Payroll &amp; PAYE</li>
    <li>Business start up assitance</li>
  </ul>

  <div class="offer">FREE Initial Consultation</div>

  <div class="brand">
    <div class="brand-dot"></div>
    <div class="brand-name">Clara Benton Accounting</div>
  </div>

  <address class="contact" style="font-style:normal">
    <p class="call">Call Today for a free initial consultation</p>
    <p class="name">CLARA BENTON ACMA, CGMA</p>
    <p class="phone">07700 900 418</p>
    <p class="email">clara@clarabentonaccounts.com</p>
    <p class="web">www.clarabentonaccounts.com</p>
  </address>
</main>
</body>
</html>
```